Truck and Van wrap design

We need designs for our trucks and vans. Our Logo and contact details including phone number (+97145917000), email (contact@dunevalegrocer.com), and website have to be incorporated into the design. Our company colors are white, green, red, and yellow in the same shades used in the logo. This design needs to be in .ai (Adobe Illustrator) format. We have 5 different size vehicles that need designs. We would prefer a scalable design that we can resize for future use.Truck 1 DimentionsHeight: 2.1 MetersWidth: 2.1 MetersLength: 5 MetersTruck 2 DimensionsHeight: 2.1 MetersWidth: 2.1 MetersLength: 4.3 MetersTruck 3 DimensionsHeight: 2.75 MetersWidth: 2.6 MetersLength: 7 MetersTrailer DimensionsHeight: 2.5 MetersWidth: 2.6 MetersLength: 13.58 MetersVan DimensionsHeight: 1.7 Meters Width: 1.7 MetersLength: 3.5 MetersYou can find pictures of the vehicles and our logo attached for reference. The trucks and trailer only need the two sides and back end designed while the van is a full wrap.
Please try to keep the designs clean and avoid the use of too many photos.

```html
<!DOCTYPE html>
<html lang="en">
<head>
<meta charset="utf-8">
<title>Dunevale Grocer – Vehicle Wrap Layouts</title>
<link rel="stylesheet" href="https://fonts.googleapis.com/css2?family=Oswald:wght@400&family=Montserrat:wght@700;800&display=swap">
<style>
  :root {
    --canvas: #e4e0db;
    --brand-red: #b5322c;
    --brand-red-deep: #9c2723;
    --brand-orange: #f5a52c;
    --brand-green: #8cbd3a;
    --brand-white: #ffffff;
    --ink: #3a3a3a;
  }
  html, body {
    margin: 0;
    padding: 0;
    width: 1200px;
    height: 1200px;
    overflow: hidden;
    background: var(--canvas);
  }
  .wrap-panel { position: absolute; display: block; }
  .wrap-panel--side-left  { left: 58px; top: 277px; width: 718px; height: 301px; }
  .wrap-panel--rear       { left: 840px; top: 277px; width: 302px; height: 301px; }
  .wrap-panel--side-right { left: 58px; top: 622px; width: 718px; height: 301px; }
  .fill-red { fill: var(--brand-red); }
  .fill-red-deep { fill: var(--brand-red-deep); }
  .fill-orange { fill: var(--brand-orange); }
  .fill-green { fill: var(--brand-green); }
  .fill-white { fill: var(--brand-white); }
  .phone { font-family: "Oswald", sans-serif; font-weight: 400; fill: var(--brand-white); }
  .company, .contact { font-family: "Montserrat", sans-serif; fill: var(--brand-white); }
  .company { font-weight: 800; }
  .contact { font-weight: 700; }
  .brand-name { font-family: "Montserrat", sans-serif; font-weight: 700; fill: var(--ink); letter-spacing: 2px; }
  .brand-dot { fill: var(--brand-red); }
</style>
</head>
<body>

<!-- Side panel, cab on the left -->
<svg class="wrap-panel wrap-panel--side-left" viewBox="0 0 897 376" preserveAspectRatio="none">
  <rect class="fill-red" width="897" height="376"/>
  <path class="fill-red-deep" d="M0,0 H100 C80,200 250,340 440,376 H0 Z"/>
  <path class="fill-orange" d="M320,0 C350,220 620,350 897,294 V0 Z"/>
  <path class="fill-white" d="M380,0 C410,200 640,320 897,280 V0 Z"/>
  <path class="fill-green" d="M447,152 C560,250 720,275 897,228 V256 C720,295 540,250 447,152 Z"/>
  <circle class="brand-dot" cx="689" cy="95" r="42"/>
  <text class="brand-name" x="689" y="192" font-size="34" text-anchor="middle">DUNEVALE</text>
  <text class="phone" x="26" y="127" font-size="50">(+97145917000)</text>
  <text class="company" x="25" y="201" font-size="28">Dunevale Grocer</text>
  <text class="company" x="25" y="237" font-size="28">General Trading LLC</text>
  <text class="contact" x="24" y="278" font-size="19">Email: contact@dunevalegrocer.com</text>
  <text class="contact" x="25" y="314" font-size="19">www.dunevalegrocer.com</text>
</svg>

<!-- Rear panel -->
<svg class="wrap-panel wrap-panel--rear" viewBox="0 0 377 376" preserveAspectRatio="none">
  <rect class="fill-red" width="377" height="376"/>
  <path class="fill-red-deep" d="M0,180 C80,300 200,360 330,376 H0 Z"/>
  <path class="fill-orange" d="M0,0 H377 V158 C300,250 120,260 0,172 Z"/>
  <path class="fill-white" d="M0,0 H377 V150 C300,232 110,232 0,105 Z"/>
  <path class="fill-green" d="M150,216 C250,218 340,170 377,100 V146 C320,206 240,222 150,216 Z"/>
  <circle class="brand-dot" cx="188" cy="75" r="30"/>
  <text class="brand-name" x="188" y="156" font-size="26" text-anchor="middle">DUNEVALE</text>
  <text class="phone" x="188" y="286" font-size="30" text-anchor="middle">(+97145917000)</text>
  <text class="company" x="188" y="310" font-size="12" text-anchor="middle">Dunevale Grocer</text>
  <text class="company" x="188" y="326" font-size="12" text-anchor="middle">General Trading LLC</text>
  <text class="contact" x="188" y="344" font-size="8" text-anchor="middle">Email: contact@dunevalegrocer.com</text>
  <text class="contact" x="188" y="359" font-size="8" text-anchor="middle">www.dunevalegrocer.com</text>
</svg>

<!-- Side panel, cab on the right -->
<svg class="wrap-panel wrap-panel--side-right" viewBox="0 0 897 376" preserveAspectRatio="none">
  <rect class="fill-red" width="897" height="376"/>
  <g transform="translate(897,0) scale(-1,1)">
    <path class="fill-red-deep" d="M0,0 H100 C80,200 250,340 440,376 H0 Z"/>
    <path class="fill-orange" d="M320,0 C350,220 620,350 897,315 V0 Z"/>
    <path class="fill-white" d="M380,0 C410,200 640,320 897,280 V0 Z"/>
    <path class="fill-green" d="M447,152 C560,250 720,275 897,232 V278 C720,300 540,250 447,152 Z"/>
  </g>
  <circle class="brand-dot" cx="207" cy="100" r="42"/>
  <text class="brand-name" x="207" y="192" font-size="34" text-anchor="middle">DUNEVALE</text>
  <text class="phone" x="872" y="126" font-size="50" text-anchor="end">(+97145917000)</text>
  <text class="company" x="872" y="202" font-size="28" text-anchor="end">Dunevale Grocer</text>
  <text class="company" x="872" y="238" font-size="28" text-anchor="end">General Trading LLC</text>
  <text class="contact" x="872" y="279" font-size="19" text-anchor="end">Email: contact@dunevalegrocer.com</text>
  <text class="contact" x="872" y="315" font-size="19" text-anchor="end">www.dunevalegrocer.com</text>
</svg>

</body>
</html>
```